Online Psychiatry business - Business Card

I need a business card design. The target audience is busy professionals of any field (this therapy appeals best to 24-35 year olds). It involves psychiatry by tele-medicine (or video-conference). Nothing on it should be a giveaway that it's about mental health. Professional design with silver or gold as the primary colors appeals to me. The card must be as simple and as uncluttered as possible. Some color and flowing design on the edge of the card appeals to me.
CrestLumaCareNet.com should probably appear in the center of the card and stand out, i.e. bold lettering, and easy to read, no cursive, but Ariel Black. Some where below this, should appear "Too Busy to Take Care of Yourself? Think again." Since this isn't office based, I don't think an office address is necessary and limits clutter.
Information that does need to appear is my name: Gerald Mewkinson, MD
General phone number: 618-472-9086. I'm hoping to get an 24-hour answering service soon so leave a little room for this. In addition I want to include two email addresses:
CrestLumaCareNet@mailvora.com and CrestLumaCare247@mailvora.com
Updates

I like the designs. I would like someone to put the website in bold in the center

 as most have been doing with a smaller font reminder nearby saying "No time" etc.
but I'd like to put my name down in the corner with the rest of the contact material.
Black print against a white or grey background appeals to me, with darker silver artwork near the sides (simple abstract, like wavy lines or something you can one up with that works. 
thanks

I ve tried to provide as much feedback as possible given my time limits, so if you have extra questions, please feel free to email. I tried to attach a file of a business card I really like but make be difficult to actually manufacture. I'm going to send you a link to the photo. The card has a pull tab. There is not much information on the outside. In fact, if you were to design the outside, I would just print : Too Busy to Take Care of Yourself? Think Again.

When you pull the tab the remaining information is on the bottom half of the card. Please don't use the color pink!!!!
http://www.printfolkgallery.net/2009/05/100-really-creative-business-cards/
It is the 39th photo on the list, about 2/3ds of the way down the page. It is titled: Ruvelinkiste

#7 and #16 have an appeal to me, except for the dot patterns
Hope this helps

I'm running out of time and energy. I 've been trying to give do down the list and give  individual feedback but I won't be able to do that anymore.

So if you have any specific questions, write me, and again thank you for all your effort!!

I know i received your files, including your zip files, Tolkra,

but Milos, did you send me the files including ZIP on project 5139624?
thanks

Target Market(s)

Working professionals and executive, attorneys, etc.

Industry/Entity Type

Business

Logo Text

Don't Have Time to Take Care of Yourself? Think Again.

Logo styles of interest
Pictorial/Combination Logo
Wordmark Logo
Font styles to use
Other font styles liked:
• Ariel Black appeals to me the most

Requirements
Must have
• Want to emphasize that the website must be obvious, easily found (The CrestLumaCareNet.com)
For that reason i'd like the card to be white, and minimal decoration on one or both sides just to add some style and color
Nice to have
• A Very uncluttered, elegant design, and something that makes it stick in your head-doesn't everyone want the last?
Should not have
• Nothing on the card that give it away that this is about psychiatry, such as brain or other symbol, but also nothing that gives it away as a medical business, such as a stethoscope or red cross or anything.

```html
<!DOCTYPE html>
<html lang="en">
<head>
<meta charset="utf-8">
<title>Business Card – Outside and Inside</title>
<link href="https://fonts.googleapis.com/css2?family=Arimo:wght@400;700&display=swap" rel="stylesheet">
<style>
  :root {
    --backdrop: #6f6f6f;
    --card-white: #ffffff;
    --silver: #ababab;
    --silver-dark: #9a9a9a;
    --ink: #333333;
    --ink-soft: #8a8a8a;
    --ink-mid: #555555;
    --on-silver: #f5f5f5;
    --perforation: #cfcfcf;
  }
  * { margin: 0; padding: 0; box-sizing: border-box; }
  html, body {
    width: 1200px;
    height: 1000px;
    overflow: hidden;
    background: var(--backdrop);
    font-family: "Arimo", Arial, sans-serif;
  }
  .card {
    position: absolute;
    width: 600px;
    height: 340px;
    background: var(--card-white);
    border-radius: 4px;
    box-shadow: 0 6px 18px rgba(0,0,0,0.3);
    overflow: hidden;
  }
  .card-outside { left: 110px; top: 110px; }
  .card-inside  { left: 490px; top: 560px; }
  .card-art {
    position: absolute;
    inset: 0;
    width: 100%;
    height: 100%;
  }
  .tagline {
    position: absolute;
    right: 26px;
    font-size: 19px;
    line-height: 22px;
    letter-spacing: 0.1px;
    white-space: nowrap;
  }
  .tagline strong { font-weight: 700; color: var(--ink); }
  .card-outside .tagline { top: 150px; color: var(--ink-soft); }
  .card-inside .tagline  { top: 150px; color: var(--ink-mid); }
  .pull-label {
    position: absolute;
    left: 46px;
    top: 214px;
    font-size: 8px;
    color: var(--ink-soft);
    letter-spacing: 1px;
    transform: rotate(90deg);
    transform-origin: left top;
  }
  .contact {
    position: absolute;
    left: 150px;
    top: 190px;
    color: var(--on-silver);
  }
  .doctor-name {
    font-weight: 700;
    font-size: 16px;
    letter-spacing: 0.6px;
    text-transform: uppercase;
    margin-left: 70px;
    margin-bottom: 8px;
    white-space: nowrap;
  }
  .contact-columns { display: flex; gap: 22px; }
  .contact-line { font-size: 12px; line-height: 19px; white-space: nowrap; }
  .phone { font-weight: 700; font-size: 15px; display: flex; align-items: center; gap: 8px; }
  .website { font-weight: 700; font-size: 15px; }
  .badge-247 {
    display: inline-flex;
    align-items: center;
    justify-content: center;
    width: 22px; height: 22px;
    border: 1.3px solid var(--on-silver);
    border-radius: 50%;
    font-size: 7px;
    font-weight: 400;
  }
</style>
</head>
<body>

  <!-- Outside of the card: tagline with pull tab -->
  <section class="card card-outside">
    <svg class="card-art" viewBox="0 0 600 340" aria-hidden="true">
      <rect x="0" y="140" width="90" height="200" fill="var(--silver)"/>
      <path d="M0 0 H600 V182 H90 C90 152 62 140 0 140 Z" fill="var(--card-white)"/>
      <path d="M90 188 H600 V266 H90 C48 266 36 250 36 227 C36 204 48 188 90 188 Z" fill="var(--card-white)"/>
      <path d="M0 340 V322 C0 302 40 292 90 292 H600 V340 Z" fill="var(--card-white)"/>
      <rect x="90" y="266" width="510" height="26" fill="var(--card-white)"/>
      <line x1="90" y1="188" x2="600" y2="188" stroke="var(--perforation)" stroke-dasharray="6 5"/>
      <line x1="90" y1="266" x2="600" y2="266" stroke="var(--perforation)" stroke-dasharray="6 5"/>
      <line x1="330" y1="100" x2="600" y2="100" stroke="var(--perforation)" stroke-dasharray="6 5"/>
    </svg>
    <p class="tagline">Too Busy to Take Care of Yourself? <strong>Think again.</strong></p>
    <span class="pull-label">PULL</span>
  </section>

  <!-- Inside of the card: contact details revealed -->
  <section class="card card-inside">
    <svg class="card-art" viewBox="0 0 600 340" aria-hidden="true">
      <rect x="0" y="150" width="600" height="140" fill="var(--silver)"/>
      <path d="M0 0 H600 V180 H100 C40 180 10 170 0 140 Z" fill="var(--card-white)"/>
      <path d="M0 340 V318 C6 300 30 290 80 290 H600 V340 Z" fill="var(--card-white)"/>
      <path d="M100 180 H600" fill="none" stroke="var(--silver-dark)" stroke-width="0.8"/>
    </svg>
    <p class="tagline">Too Busy to Take Care of Yourself? <strong>Think again.</strong></p>
    <div class="contact">
      <p class="doctor-name">Gerald Mewkinson, MD</p>
      <div class="contact-columns">
        <div>
          <p class="contact-line phone">call 618-472-9086 <span class="badge-247">24/7</span></p>
          <p class="contact-line">CrestLumaCareNet@mailvora.com</p>
        </div>
        <div>
          <p class="contact-line website">CrestLumaCareNet.com</p>
          <p class="contact-line">CrestLumaCare247@mailvora.com</p>
        </div>
      </div>
    </div>
  </section>

</body>
</html>
```